PRVD Traditional Business Card Project

Please see attached....just a simple business card... on attachment- please use the exact font, style, etc as the attached "Pat Everard Wynne" card... however, replace with the "Owen Reginald Talbot" text and address below the card.

```html
<!DOCTYPE html>
<html lang="en">
<head>
<meta charset="utf-8">
<title>PRVD Business Card – Owen Reginald Talbot</title>
<link rel="stylesheet" href="https://fonts.googleapis.com/css2?family=Tinos:wght@400&display=swap">
<style>
  :root {
    --stage: #e4e2de;
    --edge: #8c8c8c;
    --frame: #cfcfcf;
    --frame-corner: #ececec;
    --paper: #f7f7f7;
    --paper-shade: #e9e9e9;
    --ink: #151515;
    --ink-soft: #2a2a2a;
  }
  * { box-sizing: border-box; margin: 0; padding: 0; }
  html, body {
    width: 1200px; height: 780px; overflow: hidden;
    background: var(--stage);
  }
  .card {
    position: absolute; left: 75px; top: 90px;
    width: 1050px; height: 600px;
    background: var(--edge);
    padding: 16px;
    box-shadow: 0 10px 30px rgba(0,0,0,.18);
  }
  .card-frame {
    position: relative; width: 100%; height: 100%;
    background: var(--frame);
    padding: 14px;
  }
  .frame-corner {
    position: absolute; width: 34px; height: 34px;
    background: var(--frame-corner);
  }
  .frame-corner.tl { left: 0; top: 0; }
  .frame-corner.tr { right: 0; top: 0; }
  .frame-corner.bl { left: 0; bottom: 0; }
  .frame-corner.br { right: 0; bottom: 0; }
  .card-face {
    position: relative; width: 100%; height: 100%;
    background: radial-gradient(ellipse at 45% 40%, var(--paper) 0%, var(--paper) 45%, var(--paper-shade) 100%);
    font-family: "Tinos", "Times New Roman", serif;
    color: var(--ink);
  }
  .firm {
    position: absolute; left: 34px; top: 30px;
    line-height: 1.15;
  }
  .firm-name { font-size: 27px; font-variant: small-caps; letter-spacing: .5px; }
  .firm-type { font-size: 19px; text-transform: uppercase; padding-left: 26px; color: var(--ink-soft); }
  .contact {
    position: absolute; right: 34px; top: 30px;
    text-align: right; font-size: 21px; line-height: 1.25; color: var(--ink-soft);
  }
  .contact .label { text-transform: uppercase; }
  .attorney {
    position: absolute; left: 0; right: 0; top: 218px;
    text-align: center;
  }
  .attorney-name {
    font-size: 64px; font-variant: small-caps; letter-spacing: 1px; line-height: 1;
  }
  .attorney-title {
    margin-top: 10px; font-size: 22px; text-transform: uppercase; letter-spacing: 1px; color: var(--ink-soft);
  }
  .address {
    position: absolute; left: 34px; bottom: 30px;
    font-size: 21px; line-height: 1.25; color: var(--ink-soft);
  }
  .address .street, .address .city { text-transform: uppercase; }
</style>
</head>
<body>
  <div class="card">
    <div class="card-frame">
      <span class="frame-corner tl"></span>
      <span class="frame-corner tr"></span>
      <span class="frame-corner bl"></span>
      <span class="frame-corner br"></span>
      <div class="card-face">
        <div class="firm">
          <div class="firm-name">Pacific Ridge Valley</div>
          <div class="firm-type">Defense Group, PLC</div>
        </div>
        <div class="contact">
          <div><span class="label">Tel</span> (555) 210-4400</div>
          <div><span class="label">Fax</span> (555) 210-5004</div>
          <div>otalbot@prvdlaw.com</div>
        </div>
        <div class="attorney">
          <div class="attorney-name">Owen Reginald Talbot</div>
          <div class="attorney-title">Attorney at Law</div>
        </div>
        <div class="address">
          <div class="street">2740 Alder Street, Suite B</div>
          <div class="city">Cedar Bluff, CA 92000</div>
          <div class="web">www.prvdlaw.com</div>
        </div>
      </div>
    </div>
  </div>
</body>
</html>
```